Media Banner

Create a banner similar to the one in the link below showing the various media publications (TVQRN, Marlowby Ledger, Kite Wire, Pellanstroud Bulletin) and then link to "More News..."

https://www.loanvistra.com/

The bar on loan vistra is blue. Please make this bar organe to match this site:
www.bramfieldlegal.com
The bar will be used on this cite to run accross the page.

Industry/Entity Type

Graphic Design

```html
<!DOCTYPE html>
<html lang="en">
<head>
<meta charset="utf-8">
<title>Media Banner – Hartwell Firm</title>
<link href="https://fonts.googleapis.com/css2?family=Oswald:wght@400;500&family=PT+Sans+Narrow:wght@400;700&family=PT+Sans:wght@400&display=swap" rel="stylesheet">
<style>
  :root {
    --stage-dark: #2f2f2f;
    --stage-mid: #6a6a6a;
    --page-dark: #333333;
    --panel: #fafafa;
    --ink: #333333;
    --ink-soft: #8a8a8a;
    --nav-text: #9a9a9a;
    --white: #ffffff;
    --bar-top: #dcdcdc;
    --bar-mid: #8a8a8a;
    --bar-bottom: #454545;
    --social: #cfcfcf;
    --field-border: #cccccc;
    --art: #1a1a1a;
    --required: #b22222;
  }
  * { box-sizing: border-box; margin: 0; padding: 0; }
  html, body { width: 1200px; height: 1000px; overflow: hidden; }
  body { position: relative; background: var(--page-dark); font-family: "PT Sans Narrow", sans-serif; }

  .showcase {
    position: absolute; left: 0; top: 0; width: 1200px; height: 431px;
    background: radial-gradient(ellipse 700px 420px at 50% 10%, var(--stage-mid), var(--stage-dark));
  }
  .divider { position: absolute; left: 0; top: 431px; width: 1200px; height: 3px; background: var(--white); }

  .media-bar {
    position: absolute; display: flex; align-items: center;
    background: linear-gradient(to bottom, var(--bar-top) 0%, var(--bar-mid) 45%, var(--bar-bottom) 100%);
    color: var(--white); font-family: "Oswald", sans-serif;
  }
  .media-bar--large { left: 28px; top: 141px; width: 1145px; height: 90px; border: 2px solid var(--white); border-radius: 5px; padding: 0 24px 0 20px; }
  .media-bar--site { left: 93px; top: 752px; width: 1029px; height: 65px; padding: 0 22px 0 18px; }

  .media-bar__label { align-self: flex-start; font-size: 16px; font-weight: 500; letter-spacing: .3px; }
  .media-bar--large .media-bar__label { margin-top: 20px; }
  .media-bar--site .media-bar__label { margin-top: 13px; font-size: 14px; }
  .media-bar__outlets { flex: 1; display: flex; justify-content: space-around; align-items: center; }
  .outlet { font-size: 30px; font-weight: 500; white-space: nowrap; }
  .media-bar--site .outlet { font-size: 24px; }
  .media-bar__more { font-size: 18px; text-decoration: underline; color: var(--white); white-space: nowrap; }
  .media-bar--site .media-bar__more { font-size: 15px; }

  .site-header { position: absolute; left: 95px; top: 436px; width: 1027px; height: 191px; background: var(--panel); }
  .brand { position: absolute; left: 36px; top: 30px; }
  .brand__name { font-family: "PT Sans", sans-serif; font-size: 37px; color: var(--ink); letter-spacing: .5px; line-height: 1.1; }
  .brand__tagline { font-family: "PT Sans", sans-serif; font-size: 14px; color: var(--ink-soft); }
  .header-contact { position: absolute; right: 35px; top: 34px; text-align: right; color: var(--ink); }
  .header-contact__phone { font-size: 16px; font-weight: 700; }
  .header-contact__cta { margin-top: 25px; font-size: 15px; }
  .social { display: flex; gap: 11px; margin-top: 5px; justify-content: flex-end; }
  .social__item { width: 33px; height: 36px; background: var(--social); border-radius: 3px; }

  .main-nav { position: absolute; left: 116px; top: 628px; width: 981px; }
  .main-nav__pointer { position: absolute; left: 14px; top: 0; width: 0; height: 0; border-left: 5px solid transparent; border-right: 5px solid transparent; border-top: 8px solid var(--white); }
  .main-nav__row { display: flex; gap: 47px; font-size: 15px; text-transform: uppercase; color: var(--nav-text); }
  .main-nav__row--first { position: absolute; top: 27px; left: 0; width: 100%; }
  .main-nav__row--second { position: absolute; top: 85px; left: 0; }
  .main-nav__item--active { color: var(--white); }
  .main-nav__date { margin-left: auto; }

  .feature { position: absolute; top: 817px; height: 183px; background: var(--panel); }
  .feature--employment { left: 95px; width: 338px; }
  .feature--injury { left: 437px; width: 339px; }
  .feature--contact { left: 780px; width: 342px; }
  .feature__art { position: absolute; background: var(--art); }
  .feature--employment .feature__art { left: 119px; top: 38px; width: 106px; height: 145px; border-radius: 40px 40px 6px 6px; }
  .feature--injury .feature__art { left: 64px; top: 46px; width: 218px; height: 92px; border-radius: 14px; }
  .feature__title { position: absolute; left: 0; width: 100%; top: 156px; text-align: center; font-family: "PT Sans", sans-serif; font-size: 22px; color: var(--ink); }

  .contact-form__title { position: absolute; left: 127px; top: 38px; font-size: 17px; font-weight: 700; color: var(--ink); }
  .contact-form__label { position: absolute; left: 36px; top: 85px; font-size: 16px; font-weight: 700; color: var(--ink); }
  .contact-form__label span { color: var(--required); }
  .contact-form__field { position: absolute; top: 82px; width: 80px; height: 54px; border: 1px solid var(--field-border); border-radius: 3px; background: var(--white); }
  .contact-form__field--first { left: 126px; }
  .contact-form__field--last { left: 212px; }
  .contact-form__hint { position: absolute; top: 143px; font-family: "PT Sans", sans-serif; font-size: 15px; color: var(--ink-soft); }
</style>
</head>
<body>
  <section class="showcase">
    <div class="media-bar media-bar--large">
      <span class="media-bar__label">AS SEEN IN:</span>
      <div class="media-bar__outlets">
        <span class="outlet">TVQRN</span>
        <span class="outlet">Marlowby Ledger</span>
        <span class="outlet">Kite Wire</span>
        <span class="outlet">Pellanstroud Bulletin</span>
      </div>
      <a class="media-bar__more">MORE NEWS...</a>
    </div>
  </section>
  <div class="divider"></div>

  <header class="site-header">
    <div class="brand">
      <div class="brand__name">HARTWELL FIRM</div>
      <div class="brand__tagline">Employment and Injury Attorneys</div>
    </div>
    <div class="header-contact">
      <div class="header-contact__phone">555-014-2270</div>
      <div class="header-contact__cta">FREE CASE EVALUATION</div>
      <div class="social">
        <span class="social__item"></span><span class="social__item"></span><span class="social__item"></span><span class="social__item"></span><span class="social__item"></span>
      </div>
    </div>
  </header>

  <nav class="main-nav">
    <span class="main-nav__pointer"></span>
    <div class="main-nav__row main-nav__row--first">
      <span class="main-nav__item main-nav__item--active">Home</span>
      <span class="main-nav__item">Firm</span>
      <span class="main-nav__item">Blog</span>
      <span class="main-nav__item">Press</span>
      <span class="main-nav__item">Client Reviews</span>
      <span class="main-nav__item">Legal Fees</span>
      <span class="main-nav__item">Contact</span>
      <span class="main-nav__date">January 10, 2014</span>
    </div>
    <div class="main-nav__row main-nav__row--second">
      <span class="main-nav__item">Employee Rights Guide</span>
      <span class="main-nav__item">Types of Employment Cases</span>
    </div>
  </nav>

  <div class="media-bar media-bar--site">
    <span class="media-bar__label">AS SEEN IN:</span>
    <div class="media-bar__outlets">
      <span class="outlet">TVQRN</span>
      <span class="outlet">Marlowby Ledger</span>
      <span class="outlet">Kite Wire</span>
      <span class="outlet">Pellanstroud Bulletin</span>
    </div>
    <a class="media-bar__more">MORE NEWS...</a>
  </div>

  <section class="feature feature--employment">
    <div class="feature__art" role="img" aria-label="Icon of an office worker in a suit and tie"></div>
  </section>
  <section class="feature feature--injury">
    <div class="feature__art" role="img" aria-label="Icon of two cars colliding"></div>
    <h2 class="feature__title">PERSONAL INJURY CASES</h2>
  </section>
  <section class="feature feature--contact">
    <h3 class="contact-form__title">CONTACT US</h3>
    <label class="contact-form__label">Name <span>*</span></label>
    <div class="contact-form__field contact-form__field--first"></div>
    <div class="contact-form__field contact-form__field--last"></div>
    <span class="contact-form__hint" style="left:126px">First</span>
    <span class="contact-form__hint" style="left:212px">Last</span>
  </section>
</body>
</html>
```